Animal Hospital Business Cards

Make a business card look like the attached example

*Use the same blue/black coloring
*Brisket Hollow Animal Hospital (instead of pet home rounds)
*Emergency Services (instead of tamsin creek clinic)
*House Calls (instead of open 7 days by appointment)
*Change address to 278 Brisket Hollow Rd Loveland, OH 45263
*Open 7 days a week (instead of emergency service)
*Add the website www.briskethollowanimalhospital.example

On the back...
*instead of the text outlined in red, just white
*instead of the light blue, try your best to make it just like the blue and black on the front side of the card
*Delete "designed and printed by 9 whiskers inc, www.pressfeline.example

Requirements
Must have
• look just like the attached example with requested edits/changes

```html
<!DOCTYPE html>
<html lang="en">
<head>
<meta charset="utf-8">
<title>Brisket Hollow Animal Hospital – Business Card</title>
<link rel="stylesheet" href="https://fonts.googleapis.com/css2?family=Roboto:wght@500;700&family=Roboto+Condensed:wght@400;500&family=Lato:wght@400&family=Tinos:wght@700&family=Open+Sans:wght@400&display=swap">
<style>
  :root {
    --brand-blue: #287893;
    --phone-blue: #1f5a72;
    --rule-black: #111111;
    --card-white: #ffffff;
    --ink: #222222;
    --ink-soft: #444444;
    --backdrop: #6e6e6e;
  }
  * { box-sizing: border-box; margin: 0; padding: 0; }
  html, body { width: 1200px; height: 802px; overflow: hidden; }
  body { background: var(--backdrop); position: relative; font-family: "Open Sans", sans-serif; }

  .card {
    position: absolute; top: 274px; width: 442px; height: 265px;
    background: var(--card-white); overflow: hidden;
  }
  .card--front { left: 136px; }
  .card--back { left: 624px; }

  .band { position: absolute; left: 0; width: 100%; background: var(--brand-blue); color: #fff;
          display: flex; align-items: center; justify-content: center; }
  .rule { position: absolute; left: 0; width: 100%; background: var(--rule-black); }
  .txt { position: absolute; color: var(--ink); white-space: nowrap; }

  /* front */
  .card--front .band--top { top: 0; height: 54px; font: 700 19px "Roboto", sans-serif; }
  .card--front .rule--top { top: 54px; height: 5px; }
  .card--front .rule--bottom { top: 218px; height: 5px; }
  .card--front .band--bottom { top: 223px; height: 42px; font: 700 15px "Roboto", sans-serif; }

  .doctor-name { left: 0; width: 100%; top: 80px; text-align: center; font: 700 18px "Tinos", serif; color: #000; }
  .website { left: 0; width: 100%; top: 105px; text-align: center; font: 400 13px "Roboto Condensed", sans-serif; color: #000; }
  .service-emergency { left: 19px; top: 133px; font-size: 14px; line-height: 18px; }
  .species-list { left: 125px; top: 137px; font-size: 12.5px; color: var(--ink-soft); }
  .service-housecalls { left: 341px; top: 136px; font-size: 14px; }
  .address { left: 19px; top: 172px; font: 400 10.5px/14px "Roboto Condensed", sans-serif; }
  .phone-main { left: 150px; top: 178px; font: 500 23px "Roboto Condensed", sans-serif; color: var(--phone-blue); }
  .experience { left: 352px; width: 76px; top: 172px; text-align: center; font: 400 10.5px/14px "Roboto Condensed", sans-serif; }

  /* back */
  .card--back .band--top { top: 0; height: 57px; font: 400 21px "Lato", sans-serif; }
  .card--back .rule--top { top: 57px; height: 5px; }
  .card--back .rule--bottom { top: 215px; height: 5px; }
  .card--back .band--bottom { top: 220px; height: 45px; font: 400 20px "Lato", sans-serif; }

  .appt-line { font: 400 14px "Lato", sans-serif; color: var(--ink-soft); }
  .appt-for { left: 38px; top: 81px; }
  .appt-when { left: 36px; top: 118px; }
  .leader { letter-spacing: -0.5px; font-size: 12px; }
  .weekdays { position: absolute; left: 38px; top: 156px; display: flex; gap: 12px;
              font: 400 13.5px "Lato", sans-serif; color: var(--ink-soft); }
  .weekday { display: flex; align-items: center; gap: 4px; }
  .checkbox { width: 16px; height: 16px; border: 1.5px solid #555; }
</style>
</head>
<body>

<section class="card card--front" aria-label="Business card front">
  <div class="band band--top">BRISKET HOLLOW ANIMAL HOSPITAL</div>
  <div class="rule rule--top"></div>

  <p class="txt doctor-name">Gordon R.&nbsp; Palliser ,DVM</p>
  <p class="txt website">www.briskethollowanimalhospital.example</p>
  <p class="txt service-emergency">Emergency<br>Services</p>
  <p class="txt species-list">Cats • Dogs &nbsp;• &nbsp;Birds • Exotics</p>
  <p class="txt service-housecalls">House Calls</p>
  <p class="txt address">278 Brisket Hollow<br>Rd Loveland, OH 45263</p>
  <p class="txt phone-main">(513) 555-0174</p>
  <p class="txt experience">38 years of<br>experience</p>

  <div class="rule rule--bottom"></div>
  <div class="band band--bottom">OPEN 7 DAYS A WEEK</div>
</section>

<section class="card card--back" aria-label="Business card back">
  <div class="band band--top">VETERINARY APPOINTMENT</div>
  <div class="rule rule--top"></div>

  <p class="txt appt-line appt-for">YOUR APPOINTMENT FOR <span class="leader">...........................................</span>IS ON</p>
  <p class="txt appt-line appt-when">Date : <span class="leader">...............................</span> &nbsp;&nbsp; Time : <span class="leader">...........................</span> AM / PM</p>
  <div class="weekdays">
    <span class="weekday"><span class="checkbox"></span>MON</span>
    <span class="weekday"><span class="checkbox"></span>TUE</span>
    <span class="weekday"><span class="checkbox"></span>WED</span>
    <span class="weekday"><span class="checkbox"></span>THU</span>
    <span class="weekday"><span class="checkbox"></span>FRI</span>
    <span class="weekday"><span class="checkbox"></span>SAT</span>
  </div>

  <div class="rule rule--bottom"></div>
  <div class="band band--bottom">513.555.0174</div>
</section>

</body>
</html>
```